Fashion clothing business needs a label, swing tag and business card.

Independent womenswear label called "Tessa Wrenly".
I'd like a design for a woven label to go on the clothes, a swing tag and business card design. The design should be simple, modern but timeless. Its a small business, made locally in Melbourne, Australia, produces quality garments for everyday wear using beautiful fabrics.

Reason: just waiting for a few others to submit their designs.

Target Market(s)

30+ ladies, who want quality everyday wear, who don't necessarily follow trends. They can be a bit edgy and willing to take a risk with something different.

Industry/Entity Type

Clothing

Font styles to use
Other font styles liked:
• I dont mind the typewriter font, but can it look modern? happy for you to choose.

Requirements
Should not have
• A difficult shape swing tag - as it might be more expensive for me to get printed and cut.

```html
<!DOCTYPE html>
<html lang="en">
<head>
<meta charset="utf-8">
<title>Tessa Wrenly – Stationery and Labels</title>
<link rel="stylesheet" href="https://fonts.googleapis.com/css2?family=Niconne&family=Arimo:wght@400&display=swap">
<style>
  :root {
    --page: #e9e8e6;
    --ink: #141213;
    --paper-text: #f4f2f0;
    --ornament-dark: #2a2829;
    --ornament-light: #5c595a;
    --ribbon: #c3121c;
    --script: "Niconne", cursive;
    --sans: "Arimo", Arial, sans-serif;
  }
  * { box-sizing: border-box; margin: 0; padding: 0; }
  html, body { width: 1200px; height: 900px; overflow: hidden; }
  body { background: var(--page); font-family: var(--sans); color: var(--paper-text); position: relative; }

  .brand-name { font-family: var(--script); font-weight: 400; color: var(--paper-text); white-space: nowrap; }

  /* Business card */
  .business-card {
    position: absolute; left: 60px; top: 60px; width: 620px; height: 350px;
    background: var(--ink); border-radius: 4px; overflow: hidden;
  }
  .ornament {
    background: linear-gradient(160deg, var(--ornament-light), var(--ornament-dark) 70%);
    opacity: .75;
  }
  .business-card .ornament { position: absolute; left: 0; top: 0; width: 150px; height: 100%; }
  .business-card .brand-name { position: absolute; left: 200px; top: 90px; font-size: 72px; }
  .business-card .contact {
    position: absolute; right: 40px; bottom: 36px; text-align: right;
    font-size: 20px; line-height: 1.45;
  }

  /* Swing tags */
  .swing-tags { position: absolute; left: 60px; top: 470px; width: 660px; height: 400px; }
  .ribbon { position: absolute; left: 0; top: 0; width: 660px; height: 80px; }
  .swing-tag {
    position: absolute; top: 50px; width: 200px; height: 330px; background: var(--ink);
    clip-path: polygon(26% 0, 74% 0, 100% 16%, 100% 72%, 50% 100%, 0 72%, 0 16%);
  }
  .swing-tag .hole {
    position: absolute; left: 93px; top: 14px; width: 14px; height: 14px;
    border-radius: 50%; background: var(--page);
  }
  .swing-tag .ornament { position: absolute; left: 0; right: 0; bottom: 0; height: 150px; }
  .swing-tag .brand-name { position: absolute; left: 0; right: 0; top: 62px; text-align: center; font-size: 38px; }
  .swing-tag .details {
    position: absolute; left: 0; right: 0; top: 112px; text-align: center;
    font-size: 11px; line-height: 1.4;
  }
  .swing-tag .fill-in { position: absolute; left: 26px; top: 70px; font-size: 15px; line-height: 1.5; }
  .tag-left { left: 20px; }
  .tag-middle { left: 230px; top: 80px; }
  .tag-right { left: 440px; }

  /* Woven label */
  .woven-label {
    position: absolute; left: 800px; top: 370px; width: 340px; height: 130px;
    background: var(--ink); border-radius: 3px; text-align: center; padding-top: 18px;
  }
  .woven-label .brand-name { font-size: 58px; line-height: 1; }
  .woven-label .origin { font-size: 17px; margin-top: 10px; letter-spacing: .5px; }
</style>
</head>
<body>

<section class="business-card">
  <div class="ornament" role="img" aria-label="Grey floral flourish pattern along the left edge"></div>
  <h1 class="brand-name">Tessa Wrenly</h1>
  <p class="contact">mob: 0491573802<br>email: info@tessawrenly.com</p>
</section>

<section class="swing-tags">
  <svg class="ribbon" viewBox="0 0 660 80" aria-hidden="true">
    <path d="M120 75 C150 20, 250 10, 330 100" fill="none" stroke="var(--ribbon)" stroke-width="8" opacity=".8"/>
    <path d="M330 100 C360 20, 460 5, 540 75" fill="none" stroke="var(--ribbon)" stroke-width="8" opacity=".8"/>
    <path d="M300 0 L330 100 L360 0" fill="none" stroke="var(--ribbon)" stroke-width="6" opacity=".7"/>
  </svg>

  <article class="swing-tag tag-left">
    <span class="hole"></span>
    <h2 class="brand-name">Tessa Wrenly</h2>
    <p class="details">Made in Australia<br>email: info@tessawrenly.com</p>
    <div class="ornament" role="img" aria-label="Grey floral flourish pattern"></div>
  </article>

  <article class="swing-tag tag-middle">
    <span class="hole"></span>
    <p class="fill-in">Size.......<br>style......<br>Price.....</p>
    <div class="ornament" role="img" aria-label="Grey floral flourish pattern"></div>
  </article>

  <article class="swing-tag tag-right">
    <span class="hole"></span>
    <h2 class="brand-name">Tessa Wrenly</h2>
    <p class="details">Made in Australia<br>email: info@tessawrenly.com</p>
    <div class="ornament" role="img" aria-label="Grey floral flourish pattern"></div>
  </article>
</section>

<section class="woven-label">
  <h2 class="brand-name">Tessa Wrenly</h2>
  <p class="origin">Made in Australia</p>
</section>

</body>
</html>
```